Bring my website out of the dark ages!

Website redesign for Pelvano Consulting
www.pelvanoqt.example and www.mendwork.example
Currently dark (black), small font, boring, old
Want something simple, bright, fun, modern, clean and professional
Flexible content, any ideas appreciated
In business since 1998, focused on long term client relationships and being there when it matters.
Specialize solutions for clients based on their needs, vision and budget, not what the IT market thinks is the latest and greatest (and most profitable).
Want to eventually add helpful content (videos) and testimonials to the site for the benefit of the visitor

Target Market(s)

Anyone looking for IT services - target is a business with 25-100 employees.

Industry/Entity Type

It Company

Coding

Coded - Design and coding required

Number of Pages Required

4 page

Colors

Designer to choose colors to be used in the design.

Requirements
Must have
• Bright, clean, simple, no scrolling, fast
Nice to have
• Neat animation of some kind
Should not have
• scrolling
• too much information

```html
<!DOCTYPE html>
<html lang="en">
<head>
<meta charset="utf-8">
<title>Pelvano Consulting — Your Partner in Technology Solutions</title>
<link rel="stylesheet" href="https://fonts.googleapis.com/css2?family=Poppins:wght@300;400;500&display=swap">
<style>
  :root {
    --ink: #1e1e1e;
    --ink-soft: #4a4a4a;
    --on-accent: #ffffff;
    --accent: #f5a800;
    --sidebar: #ffffff;
    --muted: #8a8a8a;
    --rule: #c4c4c4;
    --ring: #3a3a3a;
    --hero-a: #f4f1ec;
    --hero-b: #e6e1d9;
    --hero-c: #d6d0c6;
  }
  * { box-sizing: border-box; margin: 0; padding: 0; }
  html, body {
    width: 1200px; height: 677px; overflow: hidden;
    background: var(--sidebar);
    font-family: "Poppins", sans-serif;
    font-weight: 300;
    color: var(--ink);
  }
  .page { position: relative; width: 1200px; height: 677px; }

  .hero-photo {
    position: absolute; left: 0; top: 0; width: 1200px; height: 677px;
    background:
      radial-gradient(ellipse 380px 300px at 640px 330px, rgba(255,255,255,0.7), transparent 70%),
      radial-gradient(ellipse 260px 420px at 1060px 400px, rgba(190,182,170,0.55), transparent 70%),
      linear-gradient(180deg, var(--hero-a) 0%, var(--hero-b) 55%, var(--hero-c) 100%);
  }

  .sidebar {
    position: absolute; left: 0; top: 0; width: 264px; height: 677px;
    background: var(--sidebar);
    box-shadow: 2px 0 18px rgba(0,0,0,0.08);
  }
  .brand {
    position: absolute; left: 40px; top: 44px;
    font-size: 19px; font-weight: 400; letter-spacing: 0.3px;
    color: var(--ink); line-height: 1.2;
  }
  .main-nav { position: absolute; left: 40px; top: 135px; width: 178px; }
  .main-nav a {
    display: flex; justify-content: space-between; align-items: center;
    height: 69.5px;
    font-size: 17.5px; color: var(--ink); text-decoration: none;
    border-bottom: 2px dotted var(--rule);
    line-height: 1;
  }
  .main-nav a:last-child { border-bottom: none; }
  .main-nav a.is-current { color: var(--accent); }
  .chevron { width: 12px; height: 8px; margin-right: 2px; }

  .follow {
    position: absolute; left: 40px; top: 542px;
    font-size: 14px; color: var(--muted);
  }
  .social { position: absolute; left: 40px; top: 577px; display: flex; gap: 12px; }
  .social a {
    display: flex; align-items: center; justify-content: center;
    width: 42px; height: 42px; border-radius: 50%;
    border: 2px solid var(--ring);
  }
  .social a svg { width: 16px; height: 16px; }
  .social a.is-active { background: var(--accent); border-color: var(--accent); }

  .phone {
    position: absolute; left: 885px; top: 37px; width: 315px; height: 53px;
    background: var(--accent);
    display: flex; align-items: center; padding-left: 34px; gap: 26px;
    font-size: 23px; font-weight: 400; letter-spacing: 1px;
    color: var(--on-accent);
  }
  .phone svg { width: 20px; height: 20px; }

  .hero-copy { position: absolute; left: 351px; top: 254px; }
  .hero-title {
    font-size: 41px; font-weight: 300; line-height: 60px; letter-spacing: 0.3px;
    color: var(--ink);
  }
  .hero-link {
    display: inline-flex; align-items: center; gap: 16px;
    margin-top: 31px;
    color: var(--accent); font-size: 17.5px; font-weight: 500; letter-spacing: 0.8px;
    text-decoration: none;
  }
  .hero-link svg { width: 20px; height: 12px; }
</style>
</head>
<body>
<div class="page">
  <div class="hero-photo" role="img" aria-label="Photo of two consultants smiling across a desk in a bright office, reviewing papers, shelves of binders behind them"></div>

  <aside class="sidebar">
    <div class="brand">Pelvano Consulting</div>

    <nav class="main-nav">
      <a href="#" class="is-current"><span>Home</span></a>
      <a href="#"><span>About Us</span></a>
      <a href="#"><span>Services</span>
        <svg class="chevron" viewBox="0 0 12 8"><path d="M1.5 1.5 6 6l4.5-4.5" fill="none" stroke="#1e1e1e" stroke-width="2"/></svg>
      </a>
      <a href="#"><span>Testimonials</span></a>
      <a href="#"><span>Contact Us</span></a>
    </nav>

    <p class="follow">Follow Us On</p>
    <div class="social">
      <a href="#" aria-label="Chat with us">
        <svg viewBox="0 0 16 16"><path d="M2 3h12v8H6l-3 3v-3H2z" fill="none" stroke="#1e1e1e" stroke-width="1.6" stroke-linejoin="round"/></svg>
      </a>
      <a href="#" aria-label="Share">
        <svg viewBox="0 0 16 16"><g fill="#1e1e1e"><circle cx="12" cy="3.5" r="2"/><circle cx="4" cy="8" r="2"/><circle cx="12" cy="12.5" r="2"/></g><path d="M12 3.5 4 8l8 4.5" fill="none" stroke="#1e1e1e" stroke-width="1.4"/></svg>
      </a>
      <a href="#" class="is-active" aria-label="Web">
        <svg viewBox="0 0 16 16"><g fill="none" stroke="#fff" stroke-width="1.5"><circle cx="8" cy="8" r="6.2"/><ellipse cx="8" cy="8" rx="2.6" ry="6.2"/><path d="M1.8 8h12.4"/></g></svg>
      </a>
    </div>
  </aside>

  <div class="phone">
    <svg viewBox="0 0 24 24"><path fill="#fff" d="M6.6 10.8a15.1 15.1 0 0 0 6.6 6.6l2.2-2.2c.3-.3.7-.4 1-.2 1.1.4 2.3.6 3.6.6.6 0 1 .4 1 1V20c0 .6-.4 1-1 1C10.6 21 3 13.4 3 4c0-.6.4-1 1-1h3.5c.6 0 1 .4 1 1 0 1.3.2 2.5.6 3.6.1.3 0 .7-.2 1z"/></svg>
    <span>555 014 2290</span>
  </div>

  <section class="hero-copy">
    <h1 class="hero-title">Your Partner in<br>Technology Solutions</h1>
    <a href="#" class="hero-link">View Details
      <svg viewBox="0 0 20 12"><path d="M0 6h17M12 1l5 5-5 5" fill="none" stroke="#1e1e1e" stroke-width="2"/></svg>
    </a>
  </section>
</div>
</body>
</html>
```